Parity Skills Forum needs a brochure to attract participants to its trainings

We need a flyer for our EU-funded project called " Parity Skills Forum" and it aims at increasing and developing skills of researchers and university staff members who are implementing measures towards gender equality in their institutions through our offered training programs. The final design should communicate gender equality for Research and Innovation centres and universities. This flyer will be distributed during conferences and events to our audience (mainly gender experts, researchers, administrative staff of universities, etc.) in order to provide the basic information about the project and options to get involved in the different trainings. We are attaching files to provide you with the concrete information on our requirements:- PS Forum flyer content.ppt: includes the content we would like to include in the flyer. There is also the URL to the project website and the different social media channels. - Project logo.zip: the project logo and guidelines as we would like to use colors that belong to the project logo color range. - Partners' logos.zip: Logos that will be included- EU flag: You can download different resolution files of the flag here: https://unionsymbols.example/about/flag_en -Regarding the images or graphics that you may include in the brochure we wouldn’t like to propose any because we do not want to limitate your imagination.

As it was not mentioned and we received a lot of questions about it, we prefer the flyer to be double-sided and in A5

Font styles to use
Serif
Sans Serif

Colors

Designer to choose colors to be used in the design.

Requirements
Nice to have
• At least 4 pages
Should not have
• We would not like to see as dominant colours the classic blue and pink.

```html
<!DOCTYPE html>
<html lang="en">
<head>
<meta charset="utf-8">
<title>Parity Skills Forum – Brochure</title>
<link rel="stylesheet" href="https://fonts.googleapis.com/css2?family=Oswald:wght@400;500&family=Roboto:wght@300;400;500&family=Montserrat:wght@400;500&display=swap">
<style>
  :root{
    --bg:#e4e4e4;
    --page-left:#f1f1f1;
    --page-right:#ffffff;
    --pink:#d3245b;
    --teal:#2bb5d3;
    --purple:#7a3d9e;
    --navy:#1f2a55;
    --ink:#333333;
    --muted:#777777;
    --rule:#7fd0e3;
    --flag:#233a8e;
  }
  *{box-sizing:border-box;margin:0;padding:0}
  html,body{width:669px;height:1200px;overflow:hidden;background:var(--bg)}
  body{position:relative;font-family:"Roboto",Arial,sans-serif;color:var(--ink)}
  .spread{position:absolute;left:25px;width:616px;display:flex;box-shadow:0 6px 14px rgba(0,0,0,.12)}
  .spread--cover{top:30px;height:472px}
  .spread--inside{top:638px;height:455px}
  .page{position:relative;width:308px;height:100%;overflow:hidden}
  .page--left{background:var(--page-left)}
  .page--right{background:var(--page-right)}

  /* Audience page */
  .heading{font-family:"Roboto",sans-serif;font-weight:500;color:var(--pink)}
  .audience-title{position:absolute;left:22px;top:20px;font-size:16px}
  .audience{position:absolute;left:16px;top:48px;width:282px;list-style:none}
  .audience .group{font-family:"Montserrat",sans-serif;font-size:8.4px;color:var(--teal);font-weight:500;letter-spacing:.3px;display:flex;align-items:center;gap:6px;margin-bottom:4px}
  .audience .group::before{content:"";width:8px;height:8px;background:var(--teal);border-radius:1px;flex:none}
  .audience .detail{font-size:7.1px;color:var(--muted);line-height:1.3;padding-left:7px;position:relative;margin-bottom:3px}
  .audience .detail::before{content:"-";position:absolute;left:0}
  .audience .group + .detail,.audience .detail + .group{margin-top:5px}
  .partners-title{position:absolute;left:22px;top:191px;font-size:13px}
  .partners{position:absolute;left:20px;top:214px;width:272px;display:grid;grid-template-columns:repeat(5,1fr);gap:11px 8px}
  .partner-badge{height:21px;background:#cfd3dc;border-radius:3px}
  .partner-badge.round{width:22px;height:22px;border-radius:50%;justify-self:center}
  .contact-title{position:absolute;left:22px;top:317px;font-size:13px}
  .contact{position:absolute;left:20px;top:345px;width:280px;font-size:8px;color:var(--ink);display:flex;flex-wrap:wrap;gap:9px 14px}
  .contact span{display:flex;align-items:center;gap:5px}
  .contact span::before{content:"";width:9px;height:9px;border-radius:50%;background:var(--teal)}
  .rule{position:absolute;height:1px;background:var(--rule)}
  .note{position:absolute;left:22px;width:264px;top:415px;text-align:center;font-size:7.6px;line-height:1.6;color:var(--ink)}
  .note a{color:var(--teal);text-decoration:none;font-weight:500}

  /* Cover */
  .photo{position:absolute;left:0;top:0;width:100%}
  .cover-photo{height:215px;background:linear-gradient(160deg,#6b5a4a,#3f3a36 55%,#8b7a68)}
  .cover-band{position:absolute;left:0;top:165px;width:308px;height:175px}
  .brand{position:absolute;left:20px;top:180px;display:flex;align-items:center;gap:14px}
  .brand-mark{width:110px;height:110px;border-radius:50%;background:#fff;border:6px solid var(--teal)}
  .brand-name{font-family:"Oswald",sans-serif;font-weight:400;font-size:21px;line-height:1.25;color:var(--pink);letter-spacing:.6px;text-transform:uppercase}
  .tagline{position:absolute;left:12px;top:332px;width:292px;font-family:"Montserrat",sans-serif;font-size:10.6px;line-height:1.5;letter-spacing:.2px;color:var(--ink)}
  .funding{position:absolute;left:15px;top:418px;display:flex;gap:8px;align-items:center}
  .flag{width:64px;height:42px;background:var(--flag)}
  .funding p{font-size:6.6px;line-height:1.4;width:212px;color:var(--ink)}

  /* Inside */
  .offer-title{position:absolute;left:0;width:100%;top:40px;text-align:center;font-family:"Oswald",sans-serif;font-size:20px;font-weight:400;color:var(--pink)}
  .offer-intro{position:absolute;left:20px;top:84px;width:272px;font-family:"Montserrat",sans-serif;font-size:9.6px;line-height:1.35;color:var(--ink)}
  .formats{position:absolute;left:10px;top:140px;width:290px;display:grid;grid-template-columns:1fr 1fr;row-gap:13px}
  .format{display:flex;flex-direction:column;align-items:center;gap:6px;height:62px}
  .format svg{width:46px;height:38px}
  .format-name{font-family:"Montserrat",sans-serif;font-size:7.8px;letter-spacing:.6px;text-transform:uppercase;text-align:center;line-height:1.3}
  .format-name.purple{color:var(--purple)} .format-name.pink{color:var(--pink)}
  .format-name.navy{color:var(--navy)} .format-name.teal{color:var(--teal)}
  .free{position:absolute;left:0;width:100%;top:393px;text-align:center;font-family:"Montserrat",sans-serif;font-size:8px;letter-spacing:.6px;color:var(--ink)}
  .free strong{color:var(--teal);font-weight:500}
  .more{position:absolute;left:0;width:100%;top:407px;text-align:center;font-family:"Montserrat",sans-serif;font-size:10.4px;color:var(--muted)}
  .url{position:absolute;left:0;width:100%;text-align:center;font-family:"Montserrat",sans-serif;font-size:14px;letter-spacing:.6px;color:var(--teal);font-weight:500}
  .group-photo{height:210px;background:linear-gradient(180deg,#cfcabf,#a39585 55%,#7e6f62)}
  .inside-band{position:absolute;left:0;top:180px;width:308px;height:65px}
  .involved-title{position:absolute;left:22px;top:260px;font-size:16px}
  .involved{position:absolute;left:10px;top:291px;list-style:none;width:292px}
  .involved li{display:flex;align-items:center;gap:7px;font-family:"Montserrat",sans-serif;font-size:8.2px;letter-spacing:.2px;margin-bottom:7px;color:var(--ink)}
  .involved li::before{content:"";width:8px;height:8px;background:var(--teal);border-radius:2px;flex:none}
  .visit{position:absolute;left:0;width:100%;top:400px;text-align:center;font-family:"Montserrat",sans-serif;font-size:10.6px;letter-spacing:.4px;color:var(--muted)}
</style>
</head>
<body>

<section class="spread spread--cover">
  <div class="page page--left">
    <h2 class="heading audience-title">Who is it for?</h2>
    <ul class="audience">
      <li class="group">Anyone interested to gender equality</li>
      <li class="group">HR Professionals Gender Trainers &amp; Experts</li>
      <li class="detail">Integration and establishment of gender-sensitive and fair recruitment and career management processes in organisations</li>
      <li class="detail">Train-the-trainers sessions for the development of new skills</li>
      <li class="group">Researcher Research Performing Organisations</li>
      <li class="detail">Training to integrate the gender dimension in their research and deepening their understanding of gender issues in R&amp;I</li>
      <li class="detail">Recommendations for influencing the internal policies and practices of the organisations towards gender equality</li>
    </ul>

    <h3 class="heading partners-title">Our Partners</h3>
    <div class="partners" aria-label="Partner organisations">
      <div class="partner-badge"></div><div class="partner-badge"></div><div class="partner-badge round"></div><div class="partner-badge round"></div><div class="partner-badge"></div>
      <div class="partner-badge"></div><div class="partner-badge"></div><div class="partner-badge"></div><div class="partner-badge"></div><div class="partner-badge"></div>
      <div class="partner-badge"></div><div class="partner-badge"></div><div class="partner-badge"></div><div class="partner-badge"></div><div class="partner-badge"></div>
    </div>

    <h3 class="heading contact-title">Contact Us</h3>
    <div class="contact">
      <span>@PSForum_eu</span>
      <span>@PSForum.eu</span>
      <span>PS Forum</span>
      <span>info@ps-forum.example</span>
      <span>www.ps-forum.example</span>
    </div>
    <div class="rule" style="left:14px;right:14px;top:402px"></div>
    <p class="note">Do you still have questions? Feel free to contact us at <a>info@ps-forum.example</a> A member of the team will make her/his best to reply as soon as possible.</p>
  </div>

  <div class="page page--right">
    <div class="photo cover-photo" role="img" aria-label="Photo of students reading and writing at a wooden table"></div>
    <svg class="cover-band" viewBox="0 0 308 175" aria-hidden="true">
      <polygon points="0,40 308,0 308,160 0,115" fill="var(--teal)"/>
      <polygon points="0,115 308,160 308,175 0,175" fill="#fff"/>
    </svg>
    <div class="brand">
      <div class="brand-mark"></div>
      <h1 class="brand-name">Parity Skills<br>Forum</h1>
    </div>
    <p class="tagline">A high quality capacity building programme on gender equality in research, innovation and higher education</p>
    <div class="rule" style="left:8px;right:8px;top:408px;background:#b8e4ee"></div>
    <div class="funding">
      <div class="flag" role="img" aria-label="Union flag"></div>
      <p>This project has received funding from the Continental Union's Frontier 2020 research and innovation programme under grant agreement No 700214.</p>
    </div>
  </div>
</section>

<section class="spread spread--inside">
  <div class="page page--left">
    <h2 class="offer-title">Training Offer</h2>
    <p class="offer-intro">Find the format and training which suits you best and apply! Different dates and locations.</p>
    <div class="formats">
      <div class="format">
        <svg viewBox="0 0 40 34" aria-hidden="true"><rect x="12" y="2" width="26" height="18" fill="none" stroke="var(--purple)" stroke-width="2"/><circle cx="7" cy="12" r="3" fill="var(--purple)"/><rect x="4" y="16" width="6" height="12" fill="var(--purple)"/><line x1="10" y1="17" x2="20" y2="10" stroke="var(--purple)" stroke-width="1.5"/><circle cx="18" cy="30" r="2.5" fill="var(--purple)"/><circle cx="26" cy="30" r="2.5" fill="var(--purple)"/><circle cx="34" cy="30" r="2.5" fill="var(--purple)"/></svg>
        <span class="format-name purple">In person-trainings</span>
      </div>
      <div class="format">
        <svg viewBox="0 0 40 34" aria-hidden="true"><rect x="10" y="1" width="20" height="12" rx="1" fill="var(--pink)"/><circle cx="20" cy="20" r="3.5" fill="var(--pink)"/><circle cx="10" cy="23" r="3" fill="var(--pink)"/><circle cx="30" cy="23" r="3" fill="var(--pink)"/><rect x="5" y="27" width="30" height="6" rx="3" fill="var(--pink)"/></svg>
        <span class="format-name pink">Workshops</span>
      </div>
      <div class="format">
        <svg viewBox="0 0 40 34" aria-hidden="true"><polygon points="20,4 38,13 20,22 2,13" fill="var(--navy)"/><path d="M10 17v8c0 3 20 3 20 0v-8l-10 5z" fill="var(--navy)"/></svg>
        <span class="format-name navy">Summer schools</span>
      </div>
      <div class="format">
        <svg viewBox="0 0 40 34" aria-hidden="true"><rect x="4" y="6" width="30" height="14" rx="7" fill="none" stroke="var(--teal)" stroke-width="2"/><circle cx="27" cy="22" r="5" fill="none" stroke="var(--teal)" stroke-width="2"/><path d="M24 26l-2 6 5-2 5 2-2-6" fill="none" stroke="var(--teal)" stroke-width="1.5"/></svg>
        <span class="format-name teal">DOCCs</span>
      </div>
      <div class="format">
        <svg viewBox="0 0 40 34" aria-hidden="true"><rect x="5" y="2" width="30" height="20" fill="none" stroke="var(--teal)" stroke-width="2"/><polygon points="17,7 25,12 17,17" fill="var(--teal)"/><line x1="20" y1="22" x2="12" y2="33" stroke="var(--teal)" stroke-width="2"/><line x1="20" y1="22" x2="28" y2="33" stroke="var(--teal)" stroke-width="2"/></svg>
        <span class="format-name teal">Webinars</span>
      </div>
      <div class="format">
        <svg viewBox="0 0 40 34" aria-hidden="true"><circle cx="9" cy="8" r="3.5" fill="var(--purple)"/><circle cx="31" cy="8" r="3.5" fill="var(--purple)"/><rect x="6" y="12" width="6" height="12" fill="var(--purple)"/><rect x="28" y="12" width="6" height="12" fill="var(--purple)"/><rect x="13" y="18" width="14" height="2.5" fill="var(--purple)"/><line x1="20" y1="20" x2="20" y2="32" stroke="var(--purple)" stroke-width="2"/></svg>
        <span class="format-name purple">Train the trainers<br>sessions</span>
      </div>
    </div>
    <div class="rule" style="left:14px;right:8px;top:384px"></div>
    <p class="free">PARTICIPATION IS <strong>FREE</strong> OF CHARGE</p>
    <p class="more">for more Training offer details please visit us at</p>
    <p class="url" style="top:424px">www.ps-forum.example</p>
  </div>

  <div class="page page--right">
    <div class="photo group-photo" role="img" aria-label="Group photo of training participants standing outside a building"></div>
    <svg class="inside-band" viewBox="0 0 308 65" aria-hidden="true">
      <polygon points="0,30 308,0 308,65 0,65" fill="var(--teal)"/>
    </svg>
    <h2 class="heading involved-title">Get Involved</h2>
    <ul class="involved">
      <li>Take part in one or more offered trainings</li>
      <li>Become a gender trainer</li>
      <li>Become a host institution to the topic of your preference</li>
      <li>Be part of the pan European gender trainers' network</li>
    </ul>
    <div class="rule" style="left:10px;right:10px;top:388px"></div>
    <p class="visit">Visit the website and find out more</p>
    <p class="url" style="top:421px">www.ps-forum.example</p>
  </div>
</section>

</body>
</html>
```